Accident Law Firm Billboard Bold Easy to See Car Accidents

We need a billboard design that can catch attention in a very crowed Car Accident lawyer market. We wish to feature the phone number (652) 318-4470 as the focus of the Bill Board. We are trying to get the phone number recognized and remembered by drivers. The law firm name is not as crucial to remember.
Basically, It's CAR ACCIDENT? Then (652) 318-4470. We are not married to any specific color scheme but it has to POP and catch attention.
So the Crucial elements are as follows:
1. Phone number (652) 318-4470
2. Words CAR ACCIDENT?
3. Firm Logo in lower portion or where appropriate. Firm Logo to be provided
4. We may want to try a Day Glow orange color, with White and Black added. An example of the color scheme shall be provided.
5. Possible "Catch Phrase" to be used, "It's Time Call 9"
Target Market(s)
Orlando Florida Car Accident victims
Industry/Entity Type
Law Firm
Requirements
Must have
- Easy to see phone number (652) 318-4470
- Catch attention
Nice to have
- I would like to have the sign visible in bright sunlight and it not too hard to immediately know what phone number is for
Should not have
- too many words
- No bold enough
- confusing fonts
- Unclear fonts

```html
<!DOCTYPE html>
<html lang="en">
<head>
<meta charset="UTF-8">
<title>Delvaro Law Firm – Car Accident Billboard</title>
<link rel="stylesheet" href="https://fonts.googleapis.com/css2?family=Anton&family=Archivo:wght@600&display=swap">
<style>
  :root {
    --frame: #3a3a3c;
    --sky: #ffffff;
    --ink: #111111;
    --road-light: #e4792a;
    --road-mid: #cf5a17;
    --road-deep: #9c3a0c;
    --wreck: #5a1e08;
    --headline: #ffffff;
  }
  * { margin: 0; padding: 0; box-sizing: border-box; }
  html, body {
    width: 1200px;
    height: 413px;
    overflow: hidden;
    background: var(--frame);
  }
  .billboard-frame {
    position: relative;
    width: 1200px;
    height: 413px;
    background: var(--frame);
  }
  .billboard {
    position: absolute;
    left: 54px;
    top: 54px;
    width: 1093px;
    height: 307px;
    overflow: hidden;
    background: var(--sky);
  }
  .crash-scene {
    position: absolute;
    left: 0;
    top: 88px;
    width: 100%;
    height: 219px;
    background:
      radial-gradient(ellipse 260px 240px at 60px 120px, var(--wreck) 0%, rgba(90,30,8,0.85) 45%, rgba(90,30,8,0) 100%),
      linear-gradient(180deg, var(--road-light) 0%, var(--road-mid) 45%, var(--road-deep) 100%);
  }
  .crash-scene.wreck-top {
    top: 40px;
    height: 48px;
    width: 240px;
    background: linear-gradient(90deg, var(--wreck) 0%, rgba(156,58,12,0.9) 60%, rgba(156,58,12,0) 100%);
    border-top-right-radius: 80px 40px;
  }
  .firm-name {
    position: absolute;
    left: 593px;
    top: 20px;
    transform: translateX(-50%);
    font-family: "Archivo", sans-serif;
    font-weight: 600;
    color: var(--ink);
    text-align: center;
    line-height: 1;
  }
  .firm-name .name-main {
    display: block;
    font-size: 40px;
    letter-spacing: 1px;
  }
  .firm-name .name-sub {
    display: block;
    font-size: 18px;
    letter-spacing: 3px;
    margin-top: 3px;
  }
  .headline, .phone {
    position: absolute;
    left: 596px;
    transform: translateX(-50%);
    font-family: "Anton", sans-serif;
    color: var(--headline);
    white-space: nowrap;
    line-height: 1;
    text-shadow: 3px 3px 4px rgba(60, 20, 0, 0.55);
  }
  .headline {
    top: 105px;
    font-size: 104px;
    letter-spacing: 1px;
  }
  .phone {
    top: 196px;
    font-size: 78px;
    letter-spacing: 1px;
  }
</style>
</head>
<body>
  <div class="billboard-frame">
    <div class="billboard">
      <div class="crash-scene" role="img" aria-label="Photo of a wrecked car on an orange-tinted open road"></div>
      <div class="crash-scene wreck-top" role="img" aria-label="Crumpled hood of the wrecked car"></div>
      <div class="firm-name">
        <span class="name-main">DELVARO</span>
        <span class="name-sub">LAW FIRM P.C.</span>
      </div>
      <h1 class="headline">CAR ACCIDENT?</h1>
      <p class="phone">(652) 318-4470</p>
    </div>
  </div>
</body>
</html>
```